Halvercott Orthodontics business card

Using our existing logo (created with ArtFolio), please create a tasteful, contemporary business card. We are father and daughter orthodontists specializing in braces, clarafit, etc to design healthy, beautiful smiles for children, adolescents, and adults. We would like the design to be family-friendly but not childish.
The final design should include all of the information without looking cluttered (I hope! If necessary to achieve an optimal design, please consider making the card double-sided)
Purple, black, silver on a white card
Please include the following information:
Halvercott Orthodontics (logo)
Marguerite L. Halvercott, DMD
Douglas R. Halvercott, DMD

312 Bramblewood Street
North Andover, MA 01899
978.555.0142

847C Quarry Hollow Street
Methuen, MA 01898
978.555.0187

email frontdesk@halvercottortho.example
website www.halvercottortho.example

```html
<!DOCTYPE html>
<html lang="en">
<head>
<meta charset="utf-8">
<title>Halvercott Orthodontics business card</title>
<link rel="stylesheet" href="https://fonts.googleapis.com/css2?family=Figtree:wght@400;600;700&display=swap">
<style>
  :root {
    --purple: #5a2587;
    --purple-band: #53217e;
    --grey-text: #5e5e5e;
    --grey-band: #6f7070;
    --rule: #7a7a7a;
    --card: #f7f7f7;
    --backdrop: #d9dcdb;
    --white: #ffffff;
  }
  * { box-sizing: border-box; margin: 0; padding: 0; }
  html, body {
    width: 1200px; height: 1200px; overflow: hidden;
    background: var(--backdrop);
    font-family: "Figtree", Arial, sans-serif;
  }
  .stage { position: relative; width: 1200px; height: 1200px; }
  .card {
    position: absolute; left: 236px; width: 728px; height: 416px;
    background: var(--card); border-radius: 4px; overflow: hidden;
    box-shadow: 0 10px 30px rgba(0,0,0,0.18);
  }
  .card--back { top: 134px; }
  .card--front { top: 620px; }

  /* brand name */
  .brand { position: absolute; display: flex; align-items: center; color: var(--purple); font-weight: 600; }
  .brand__dot { border-radius: 50%; background: var(--purple); flex: none; }
  .brand__text { display: flex; flex-direction: column; line-height: 1; }
  .brand__name { letter-spacing: 0.02em; }
  .brand__sub { text-transform: uppercase; }

  .card--back .brand { right: 44px; top: 52px; gap: 12px; }
  .card--back .brand__dot { width: 40px; height: 40px; }
  .card--back .brand__name { font-size: 36px; }
  .card--back .brand__sub { font-size: 12.5px; letter-spacing: 0.42em; margin-top: 6px; }

  .card--front .brand { left: 50%; top: 146px; transform: translateX(-50%); gap: 22px; }
  .card--front .brand__dot { width: 84px; height: 84px; }
  .card--front .brand__name { font-size: 70px; }
  .card--front .brand__sub { font-size: 24px; letter-spacing: 0.47em; margin-top: 10px; }

  /* doctors */
  .doctors { position: absolute; left: 45px; top: 206px; color: var(--purple); font-weight: 700; font-size: 20px; }
  .doctors__name { line-height: 1; }
  .doctors__rule { width: 100%; height: 2px; background: var(--rule); margin: 10px 0 11px; }

  /* contacts */
  .contacts { position: absolute; left: 43px; top: 293px; list-style: none; color: var(--grey-text); font-size: 18px; }
  .contacts li { display: flex; align-items: center; gap: 10px; height: 28px; }
  .icon { width: 16px; height: 16px; flex: none; fill: var(--purple); }

  .address { position: absolute; right: 44px; top: 321px; text-align: right; font-style: normal; color: var(--grey-text); font-size: 18px; line-height: 28px; }

  .footer-strip { position: absolute; left: 0; bottom: 0; width: 100%; height: 16px; display: flex; }
  .footer-strip__grey { width: 391px; background: var(--grey-band); }
  .footer-strip__purple { flex: 1; background: var(--purple); }

  /* front band */
  .front-band { position: absolute; left: 0; bottom: 0; width: 728px; height: 76px; }
  .front-contacts { position: absolute; left: 50px; bottom: 12px; list-style: none; color: var(--white); font-size: 19.5px; }
  .front-contacts li { display: flex; align-items: center; gap: 10px; height: 29px; }
  .front-contacts .icon { fill: var(--white); }
</style>
</head>
<body>
<main class="stage">

  <section class="card card--back" aria-label="Business card contact side">
    <div class="brand">
      <span class="brand__dot"></span>
      <div class="brand__text">
        <span class="brand__name">HALVERCOTT</span>
        <span class="brand__sub">Orthodontics</span>
      </div>
    </div>

    <div class="doctors">
      <p class="doctors__name">Marguerite L. Halvercott, DMD</p>
      <div class="doctors__rule"></div>
      <p class="doctors__name">Douglas R. Halvercott, DMD</p>
    </div>

    <ul class="contacts">
      <li>
        <svg class="icon" viewBox="0 0 24 24"><path d="M6.6 10.8a15.2 15.2 0 0 0 6.6 6.6l2.2-2.2a1 1 0 0 1 1-.25 11.4 11.4 0 0 0 3.6.57 1 1 0 0 1 1 1V20a1 1 0 0 1-1 1A17 17 0 0 1 3 4a1 1 0 0 1 1-1h3.5a1 1 0 0 1 1 1c0 1.25.2 2.45.57 3.57a1 1 0 0 1-.25 1z"/></svg>
        <span>978-555-0187</span>
      </li>
      <li>
        <svg class="icon" viewBox="0 0 24 24"><path d="M2 5h20v14H2z M3.5 6.5 12 13l8.5-6.5" fill="var(--purple)"/><path d="M3.5 6.5 12 13l8.5-6.5" fill="none" stroke="#f7f7f7" stroke-width="1.6"/></svg>
        <span>frontdesk@halvercottortho.example</span>
      </li>
      <li>
        <svg class="icon" viewBox="0 0 24 24"><circle cx="12" cy="12" r="10"/><path d="M2 12h20M12 2c3 3 3 17 0 20M12 2c-3 3-3 17 0 20" fill="none" stroke="#f7f7f7" stroke-width="1.5"/></svg>
        <span>www.halvercottortho.example</span>
      </li>
    </ul>

    <address class="address">
      847C Quarry Hollow St.<br>
      Methuen, MA 01898
    </address>

    <div class="footer-strip">
      <span class="footer-strip__grey"></span>
      <span class="footer-strip__purple"></span>
    </div>
  </section>

  <section class="card card--front" aria-label="Business card brand side">
    <div class="brand">
      <span class="brand__dot"></span>
      <div class="brand__text">
        <span class="brand__name">HALVERCOTT</span>
        <span class="brand__sub">Orthodontics</span>
      </div>
    </div>

    <svg class="front-band" viewBox="0 0 728 76" preserveAspectRatio="none" aria-hidden="true">
      <path d="M0 0 H636 C690 0 722 38 728 76 H0 Z" fill="var(--purple-band)"/>
    </svg>

    <ul class="front-contacts">
      <li>
        <svg class="icon" viewBox="0 0 24 24"><path d="M12 2a7 7 0 0 0-7 7c0 5.2 7 13 7 13s7-7.8 7-13a7 7 0 0 0-7-7zm0 9.5A2.5 2.5 0 1 1 12 6.5a2.5 2.5 0 0 1 0 5z"/></svg>
        <span>312 Bramblewood St. North Andover, MA 01899</span>
      </li>
      <li>
        <svg class="icon" viewBox="0 0 24 24"><path d="M6.6 10.8a15.2 15.2 0 0 0 6.6 6.6l2.2-2.2a1 1 0 0 1 1-.25 11.4 11.4 0 0 0 3.6.57 1 1 0 0 1 1 1V20a1 1 0 0 1-1 1A17 17 0 0 1 3 4a1 1 0 0 1 1-1h3.5a1 1 0 0 1 1 1c0 1.25.2 2.45.57 3.57a1 1 0 0 1-.25 1z"/></svg>
        <span>978-555-0142</span>
      </li>
    </ul>
  </section>

</main>
</body>
</html>
```